Summit Shield Coatings Inc facebook rebranding

We had our facebook design done 3 years ago and we need to get it more updated and attractive. I have attached what we already use and here below is a link to our page. i have 2 locations so when we pick a design we will need files to have each locations logo and phone number
location 1- Summit Shield Coatings Inc. 469-555-0148
Location 2- Summit Shield Coatings of west texas inc. 806-555-0192
here is link
Target Market(s)
contractors and homeowners
Industry/Entity Type
Insulation
Font styles to use
Serif
Colors
0054AA
0677BA
7BADD7
CADEEF
E8F1F8

```html
<!DOCTYPE html>
<html lang="en">
<head>
<meta charset="UTF-8">
<title>Summit Shield Coatings Inc – Cover</title>
<link href="https://fonts.googleapis.com/css2?family=Abril+Fatface&family=Cormorant+SC:wght@700&family=Encode+Sans+Condensed:wght@500&display=swap" rel="stylesheet">
<style>
  :root {
    --navy-deep: #02070f;
    --blue-edge: #0e4a98;
    --blue-ring: #1356a8;
    --blue-mid: #0677BA;
    --blue-soft: #7BADD7;
    --blue-pale: #CADEEF;
    --white-ice: #E8F1F8;
  }
  * { margin: 0; padding: 0; box-sizing: border-box; }
  html, body { width: 1200px; height: 676px; overflow: hidden; background: var(--navy-deep); }
  .cover {
    position: relative;
    width: 1200px;
    height: 676px;
    overflow: hidden;
    background: linear-gradient(90deg, var(--blue-edge) 0%, #06244a 30%, var(--navy-deep) 50%, #06244a 72%, var(--blue-edge) 100%);
  }
  .decor { position: absolute; inset: 0; }
  .tagline {
    position: absolute;
    left: 440px; width: 680px; top: 120px;
    text-align: center;
    font-family: "Cormorant SC", serif;
    font-weight: 700;
    font-size: 24px;
    letter-spacing: 3px;
    color: var(--blue-pale);
  }
  .services {
    position: absolute;
    left: 440px; width: 680px; top: 160px;
    text-align: center;
    font-family: "Encode Sans Condensed", sans-serif;
    font-weight: 500;
    font-size: 35px;
    color: var(--blue-pale);
    text-shadow: 0 0 6px rgba(123,173,215,0.9), 0 0 14px rgba(6,119,186,0.8);
    word-spacing: 6px;
  }
  .services .sep { margin: 0 10px; }
  .contact-title, .contact-phone {
    position: absolute;
    left: 300px; width: 640px;
    text-align: center;
    font-family: "Abril Fatface", serif;
    color: var(--white-ice);
    letter-spacing: 5px;
  }
  .contact-title { top: 255px; font-size: 70px; }
  .contact-phone { top: 350px; font-size: 72px; }
  .web-pill {
    position: absolute;
    left: 383px; top: 474px;
    width: 429px; height: 84px;
    border-radius: 42px;
    background: var(--blue-soft);
    display: flex; align-items: center; justify-content: center;
    font-family: "Encode Sans Condensed", sans-serif;
    font-weight: 500;
    font-size: 29px;
    letter-spacing: 1px;
    color: #ffffff;
  }
</style>
</head>
<body>
<main class="cover">
  <svg class="decor" width="1200" height="676" viewBox="0 0 1200 676">
    <defs>
      <linearGradient id="installerTone" x1="0" y1="0" x2="1" y2="1">
        <stop offset="0" stop-color="#b08a5c"/>
        <stop offset="0.5" stop-color="#3d4766"/>
        <stop offset="1" stop-color="#8c8478"/>
      </linearGradient>
      <linearGradient id="roomTone" x1="0" y1="0" x2="0" y2="1">
        <stop offset="0" stop-color="#a67c55"/>
        <stop offset="0.55" stop-color="#e6d9c3"/>
        <stop offset="1" stop-color="#b6aa99"/>
      </linearGradient>
    </defs>
    <circle class="corner-disc" cx="1039" cy="0" r="80" fill="var(--blue-ring)"/>
    <circle class="corner-disc" cx="1142" cy="645" r="75" fill="var(--blue-ring)"/>
    <circle class="bottom-ring" cx="198" cy="660" r="95" fill="none" stroke="var(--blue-ring)" stroke-width="32"/>
    <circle class="photo-frame" cx="128" cy="220" r="280" fill="var(--blue-ring)"/>
    <circle class="photo-frame" cx="1028" cy="498" r="165" fill="var(--blue-ring)"/>
    <circle role="img" aria-label="Installer in protective suit spraying foam insulation on wall sheathing" cx="128" cy="220" r="252" fill="url(#installerTone)"/>
    <circle role="img" aria-label="Framed room with walls filled with sprayed foam insulation" cx="1028" cy="498" r="140" fill="url(#roomTone)"/>
    <circle class="dot-ring" cx="451" cy="111" r="8" fill="none" stroke="var(--blue-ring)" stroke-width="7"/>
    <circle class="dot-ring" cx="293" cy="457" r="21" fill="none" stroke="var(--blue-ring)" stroke-width="17"/>
    <circle class="dot-ring" cx="79" cy="569" r="8" fill="none" stroke="var(--blue-ring)" stroke-width="7"/>
    <circle class="dot-ring" cx="830" cy="627" r="21" fill="none" stroke="var(--blue-ring)" stroke-width="17"/>
  </svg>

  <p class="tagline">DFW PREMIER INSULATION COMPANY</p>
  <p class="services">Spray foam<span class="sep">-</span>Fiberglass<span class="sep">-</span>Insulation<span class="sep">-</span>Roofing</p>
  <h1 class="contact-title">CONTACT US:</h1>
  <p class="contact-phone">469-555-0148</p>
  <div class="web-pill">summitshieldcoatings.com</div>
</main>
</body>
</html>
```